Viral Marketing Software - Web Application Design

*****UPDATE******
Thank you all for your submissions but we would like to see more of a variety in these designs. It seems as though every design we have received has been almost identical to the mock up we provided. We would like to see more creativity. The mock up provided was meant to be used as an example not a format. We would appreciate if you could show us
1. Logo for Ripple Kindler
2. Home page design
3. Coupon Manager design

* Please refer to this link to see what our coupon manager page looks like.
http://qtrplaza.net/briefhub.html (use only as example please do not copy)
*******************************************************

We need a web design for a company based just outside of Austin, Texas called 'Ripple Kindler'. We have designed a viral marketing platform that harnesses the power of social media to spread promotions through people's social networks.

We have developed a working prototype here: http://qtrplaza.net

We originally went with a fun and young identity while we were testing, but we are shifting our focus to a more professional b2b product. Our name originally was Pals n/Perks and our designed catered more towards the end-users of our product (the people receiving the promotions) - now, we'd like to change out identity and our branding to focus more on the businesses purchasing our product. So, we've changed our name to Ripple Kindler and we are looking for a very slick and professional design to go with our new name.

We like the look of these two sites:

http://shiftlark.com
http://mailorbitly.com

To imitate the design from shiftlark.com with our software, I've created this mock-up:

http://qtrplaza.net/ripplekindler

We like these clean, professional design examples. These examples should only be used as a point of reference.

We will have approx. 8 screens in total that we will need designs for. For now, please create a web design and logo for Ripple Kindler based on these two pages:

Home Page & Promo Manager - http://qtrplaza.net/briefhub.html

Thank you!!!
Updates

Reason: we have not gotten enough designs to choose from yet to make our decision

Reason: We have not received enough unique submissions.

Thank you all for your submissions! Please recheck our brief as we have updated it.

For all the designers that have submitted designs for our project please go look at our likes and dislikes that I have uploaded. We have narrowed it down to 3 designers. Can you take our feedback into consideration and give us a more refined revision of your work and we will move forward from there. We would like to wrap this project up very soon. Thanks!                                   

Reason: We have narrowed our project submissions down to 3 designers. Please read our new posting and view our uploaded examples and what we like about each and please give us some revisions. We would like to get this project finished very soon. Thank You!

Target Market(s)

Small to Medium-Sized Business owners who are looking at marketing their business online.

Industry/Entity Type

It Company

Requirements
Must have
• Clean-professional look

Logo for Ripple Kindler

```html
<!DOCTYPE html>
<html lang="en">
<head>
<meta charset="utf-8">
<title>Ripple Kindler</title>
<link href="https://fonts.googleapis.com/css2?family=Arimo:wght@400;700&display=swap" rel="stylesheet">
<style>
:root{
  --ink:#2b2b2b;
  --muted:#6b6b6b;
  --page:#ececec;
  --white:#ffffff;
  --slider-top:#5a5a5a;
  --slider-bot:#2f2f2f;
  --accent:#c8202a;
  --footer:#242424;
  --footer-deep:#181818;
  --footer-text:#b9b9b9;
  --line:#d4d4d4;
}
*{margin:0;padding:0;box-sizing:border-box}
html,body{width:882px;height:1200px;overflow:hidden}
body{font-family:"Arimo",Arial,sans-serif;background:var(--page);color:var(--ink);position:relative}

/* header */
.site-header{height:88px;background:var(--white);display:flex;align-items:center;justify-content:space-between;padding:0 24px 0 22px;border-bottom:1px solid var(--line)}
.brand{display:flex;align-items:center;gap:10px;font-size:30px;font-weight:700;color:var(--ink)}
.brand-mark{width:30px;height:30px;background:var(--accent);border-radius:50%}
.main-nav{display:flex;align-items:center;gap:6px;font-size:13px}
.main-nav a{color:var(--ink);text-decoration:none;padding:7px 12px}
.main-nav .home{width:34px;height:30px;background:#e8e8e8;border-radius:3px;display:flex;align-items:center;justify-content:center;padding:0}
.main-nav .account{border:1px solid #cfcfcf;border-radius:3px;background:#f4f4f4}

/* slider */
.showcase{height:274px;background:linear-gradient(var(--slider-top),var(--slider-bot));position:relative}
.showcase-arrow{position:absolute;top:160px;width:20px;height:28px;background:#8a8a8a;display:flex;align-items:center;justify-content:center}
.showcase-arrow.prev{left:10px}.showcase-arrow.next{right:10px}
.screen{position:absolute;top:60px;width:234px;height:148px;background:var(--white);border:4px solid #d9d9d9;box-shadow:0 4px 10px rgba(0,0,0,.4);padding:5px}
.screen-bar{height:10px;background:#3a3a3a;margin-bottom:4px}
.screen table{width:100%;border-collapse:collapse;font-size:5px;color:#334}
.screen th{background:#dfe6ee;height:10px;border:1px solid #c8d0da}
.screen td{border:1px solid #dde3ea;height:19px;padding:1px 2px;color:#2b5fa8}
.showcase-close{height:34px;background:linear-gradient(#dcdcdc,#c4c4c4);display:flex;justify-content:center}
.showcase-close span{background:#f3f3f3;font-size:8px;font-weight:700;letter-spacing:.5px;padding:4px 14px;height:17px;border-radius:0 0 4px 4px}

/* section titles */
.section-title{display:flex;align-items:center;gap:12px;margin:16px 24px 0;font-size:12px;color:var(--muted);letter-spacing:.5px}
.section-title::before,.section-title::after{content:"";flex:1;height:1px;background:#c8c8c8}

/* service cards */
.services{display:grid;grid-template-columns:repeat(4,1fr);gap:8px;margin:14px 24px 0;height:250px}
.service-card{background:var(--white);border:1px solid #dadada}
.service-card h3{font-size:14px;text-align:center;padding:12px 0 10px;background:linear-gradient(#fafafa,#e9e9e9);text-transform:uppercase}
.service-image{height:96px;margin:0 8px}
.service-card p{font-size:9px;color:var(--muted);line-height:1.4;margin:10px 10px 6px}
.read-more{font-size:9px;color:var(--accent);margin-left:10px;text-decoration:none}

/* partners */
.partners{height:110px;margin:14px 0 0;background:var(--white);display:flex;align-items:center;justify-content:space-around;padding:0 40px;border-top:1px solid var(--line);border-bottom:1px solid var(--line)}
.partner{font-size:17px;font-weight:700;color:var(--ink)}
.partner-badge{width:60px;height:60px;background:#6b6b6b;border-radius:4px}
.pager{display:flex;justify-content:center;gap:5px;margin:8px 0}
.pager i{width:8px;height:8px;border-radius:50%;background:#bdbdbd}
.pager i.on{background:var(--accent)}

/* footer */
.site-footer{position:absolute;left:0;right:0;bottom:0;height:240px;background:var(--footer);color:var(--footer-text)}
.footer-cols{display:grid;grid-template-columns:150px 170px 170px 170px 1fr;padding:22px 24px 0}
.footer-cols h4{color:var(--white);font-size:12px;margin-bottom:12px}
.footer-cols li{list-style:none;font-size:10px;margin-bottom:7px}
.footer-cols li::before{content:"› ";color:var(--white)}
.social{display:flex;gap:8px}
.social i{width:22px;height:22px;border-radius:50%;background:#e5e5e5}
.copyright{position:absolute;bottom:0;left:0;right:0;height:38px;background:var(--footer-deep);font-size:9px;text-align:center;line-height:38px}
</style>
</head>
<body>
<header class="site-header">
  <div class="brand"><span class="brand-mark"></span>Ripple Kindler</div>
  <nav class="main-nav">
    <a class="home" href="#" aria-label="Home"><svg width="16" height="14" viewBox="0 0 16 14"><path d="M8 1 1 7h2v6h4V9h2v4h4V7h2z" fill="#444"/></svg></a>
    <a href="#">Tour</a><a href="#">Viral Marketing</a><a href="#">Lead Generation</a><a href="#">Packages</a>
    <a class="account" href="#">Sign Up</a><a class="account" href="#">Login</a>
  </nav>
</header>

<section class="showcase">
  <div class="showcase-arrow prev"><svg width="8" height="10"><path d="M7 0 0 5l7 5z" fill="#fff"/></svg></div>
  <div class="showcase-arrow next"><svg width="8" height="10"><path d="M1 0l7 5-7 5z" fill="#fff"/></svg></div>
  <div class="screen" style="left:53px">
    <div class="screen-bar"></div>
    <table><tr><th>Promo</th><th>Status</th><th>Views</th><th>Shares</th><th>Chart</th></tr>
    <tr><td>Spring deal</td><td>Active</td><td>320</td><td>41</td><td></td></tr>
    <tr><td>Free coffee</td><td>Active</td><td>210</td><td>28</td><td></td></tr>
    <tr><td>Half off</td><td>Paused</td><td>95</td><td>12</td><td></td></tr>
    <tr><td>Gift card</td><td>Ended</td><td>480</td><td>66</td><td></td></tr></table>
  </div>
  <div class="screen" style="left:323px">
    <div class="screen-bar"></div>
    <table><tr><th>Promo</th><th>Status</th><th>Views</th><th>Shares</th><th>Chart</th></tr>
    <tr><td>Spring deal</td><td>Active</td><td>320</td><td>41</td><td></td></tr>
    <tr><td>Free coffee</td><td>Active</td><td>210</td><td>28</td><td></td></tr>
    <tr><td>Half off</td><td>Paused</td><td>95</td><td>12</td><td></td></tr>
    <tr><td>Gift card</td><td>Ended</td><td>480</td><td>66</td><td></td></tr></table>
  </div>
  <div class="screen" style="left:591px">
    <div class="screen-bar"></div>
    <table><tr><th>Promo</th><th>Status</th><th>Views</th><th>Shares</th><th>Chart</th></tr>
    <tr><td>Spring deal</td><td>Active</td><td>320</td><td>41</td><td></td></tr>
    <tr><td>Free coffee</td><td>Active</td><td>210</td><td>28</td><td></td></tr>
    <tr><td>Half off</td><td>Paused</td><td>95</td><td>12</td><td></td></tr>
    <tr><td>Gift card</td><td>Ended</td><td>480</td><td>66</td><td></td></tr></table>
  </div>
</section>
<div class="showcase-close"><span>CLICK TO CLOSE WINDOW</span></div>

<h2 class="section-title">OUR SERVICES</h2>
<section class="services">
  <article class="service-card">
    <h3>Grow Business</h3>
    <div class="service-image" role="img" aria-label="Laptop showing a rising growth chart" style="background:linear-gradient(#f2f2f2,#bcbcbc)"></div>
    <p>Lorem ipsum dolor sit amet elit dolor amet nunc lacinia dui turpis sed vitae.</p>
    <a class="read-more" href="#">Read More »</a>
  </article>
  <article class="service-card">
    <h3>Social Campaigns</h3>
    <div class="service-image" role="img" aria-label="Blue glowing at-sign on a digital background" style="background:linear-gradient(#5b8ec4,#173f72)"></div>
    <p>Lorem ipsum dolor sit amet elit dolor amet nunc lacinia dui turpis sed vitae.</p>
    <a class="read-more" href="#">Read More »</a>
  </article>
  <article class="service-card">
    <h3>Our Clients</h3>
    <div class="service-image" role="img" aria-label="Business people meeting at a table" style="background:linear-gradient(#b8b2a8,#4e4a45)"></div>
    <p>Lorem ipsum dolor sit amet elit dolor amet nunc lacinia dui turpis sed vitae.</p>
    <a class="read-more" href="#">Read More »</a>
  </article>
  <article class="service-card">
    <h3>Contact Us</h3>
    <div class="service-image" role="img" aria-label="Support agent wearing a headset" style="background:linear-gradient(#e6e2dc,#8a7260)"></div>
    <p>Lorem ipsum dolor sit amet elit dolor amet nunc lacinia dui turpis sed vitae.</p>
    <a class="read-more" href="#">Read More »</a>
  </article>
</section>

<h2 class="section-title">OUR PARTNERS</h2>
<section class="partners">
  <div class="partner-badge" role="img" aria-label="Partner badge"></div>
  <div class="partner">Colbert's</div>
  <div class="partner">HALVERN COLLEGE</div>
  <div class="partner">Kneadwell Spa</div>
  <div class="partner">Bram &amp; Joss</div>
</section>
<div class="pager"><i></i><i class="on"></i><i></i></div>

<footer class="site-footer">
  <div class="footer-cols">
    <div><h4>Quick Link</h4><ul><li>Social Marketing</li><li>Email Marketing</li><li>Local Search</li><li>Online Survey</li><li>Pe Industry</li></ul></div>
    <div><h4>Special Informations</h4><ul><li>About Us</li><li>Our Team</li><li>Company Locations</li><li>Testimonials</li><li>Careers</li></ul></div>
    <div><h4>Software Informations</h4><ul><li>Software Charts</li><li>Featured Service</li><li>Demo Tour</li><li>Softwares</li><li>Demo Installation</li></ul></div>
    <div><h4>Support</h4><ul><li>Customer Support</li><li>FAQs</li><li>Contact Us</li><li>Blog</li></ul></div>
    <div><h4>KEEP IN TOUCH</h4><div class="social"><i></i><i></i><i></i><i></i></div></div>
  </div>
  <div class="copyright">©2012, Ripplekindler.com, All Rights Reserved &nbsp;|&nbsp; Terms &amp; Conditions</div>
</footer>
</body>
</html>
```